SHG business cards

design a business card

(Generators . Lighting Towers . De-watering Pumps . Compressors) put under the logo please. my details are Marek Oyelaran (Director) 0461527308 silverpinehaulgroup@postvane.com

```html
<!DOCTYPE html>
<html lang="en">
<head>
<meta charset="utf-8">
<title>SHG Business Cards</title>
<link href="https://fonts.googleapis.com/css2?family=Jost:wght@400;500;600&display=swap" rel="stylesheet">
<style>
  :root {
    --backdrop: #2a2a2b;
    --card: #ffffff;
    --gold: #c98a2b;
    --ink: #3f3f42;
    --rule-grey: #8a8a8d;
  }
  * { box-sizing: border-box; margin: 0; padding: 0; }
  html, body {
    width: 1200px; height: 900px; overflow: hidden;
    background: var(--backdrop);
    font-family: "Jost", sans-serif;
  }
  .stage {
    width: 1200px; height: 900px;
    display: flex; flex-direction: column; align-items: center; justify-content: center;
    gap: 44px;
  }
  .card {
    position: relative;
    width: 640px; height: 366px;
    background: linear-gradient(135deg, #f1f1f1 0%, var(--card) 55%);
    box-shadow: 0 10px 24px rgba(0,0,0,.45);
  }
  .brand {
    display: flex; align-items: center; gap: 12px;
  }
  .brand-mark {
    width: 22px; height: 22px; background: var(--gold);
  }
  .brand-name {
    font-weight: 600; color: var(--gold);
    letter-spacing: .04em; text-transform: uppercase; white-space: nowrap;
  }

  /* front */
  .card-front .content {
    position: absolute; inset: 0;
    display: flex; flex-direction: column; align-items: center; justify-content: center;
  }
  .card-front .brand-name { font-size: 30px; }
  .card-front .rule {
    width: 330px; height: 1px; background: var(--gold); margin: 16px 0 12px;
  }
  .services-stack {
    text-align: center; color: var(--ink); font-weight: 500;
    font-size: 17px; line-height: 1.3;
  }

  /* back */
  .card-back .brand {
    position: absolute; top: 58px; right: 62px;
  }
  .card-back .brand-name { font-size: 26px; }
  .card-back .brand-rule {
    position: absolute; top: 102px; right: 62px; width: 330px; height: 1px; background: var(--rule-grey);
  }
  .contact {
    position: absolute; left: 48px; top: 190px; color: var(--ink);
  }
  .person-name { font-size: 24px; font-weight: 600; color: var(--gold); line-height: 1.1; }
  .person-role { font-size: 18px; margin-bottom: 14px; }
  .contact-line {
    display: flex; align-items: center; gap: 10px; font-size: 17px; line-height: 1.55;
  }
  .contact-line svg { width: 16px; height: 16px; fill: none; stroke: #6b6b6e; stroke-width: 1.6; }
  .card-back .footer-rule {
    position: absolute; left: 48px; right: 48px; bottom: 52px; height: 1px; background: var(--rule-grey);
  }
  .services-line {
    position: absolute; left: 48px; right: 48px; bottom: 20px;
    font-size: 17px; font-weight: 600; color: var(--gold); white-space: nowrap;
  }
</style>
</head>
<body>
<main class="stage">
  <section class="card card-front">
    <div class="content">
      <div class="brand">
        <span class="brand-mark"></span>
        <span class="brand-name">Silverpine Haul Group</span>
      </div>
      <div class="rule"></div>
      <p class="services-stack">Generators . Lighting Towers<br>De-watering Pumps . Compressors</p>
    </div>
  </section>

  <section class="card card-back">
    <div class="brand">
      <span class="brand-mark"></span>
      <span class="brand-name">Silverpine Haul Group</span>
    </div>
    <div class="brand-rule"></div>

    <div class="contact">
      <p class="person-name">Marek Oyelaran</p>
      <p class="person-role">Director</p>
      <p class="contact-line">
        <svg viewBox="0 0 16 16" aria-hidden="true"><path d="M4 1.5l2.2 3-1.4 1.6c.8 1.8 2.3 3.3 4.1 4.1l1.6-1.4 3 2.2-1.3 2.4C7 13.2 2.8 9 2 3.3z"/></svg>
        0461527308
      </p>
      <p class="contact-line">
        <svg viewBox="0 0 16 16" aria-hidden="true"><rect x="1.5" y="3.5" width="13" height="9"/><path d="M1.5 3.5l6.5 5 6.5-5"/></svg>
        silverpinehaulgroup@postvane.com
      </p>
    </div>

    <div class="footer-rule"></div>
    <p class="services-line">Generators . Lighting Towers . De-watering Pumps . Compressors</p>
  </section>
</main>
</body>
</html>
```